Book Cover - The Velvet Lantern Almanac Collection

We are writing a book about the velvet lantern almanac collection, including Guerrilla Marketing. Advertising, Branding and PR.

We are looking for a fun and quirky cover, and are open to your ideas 💡
My website and social media are on www.TorvanPelica.co and posts are shared on Trelvano. Again we are open to ideas

```html
<!DOCTYPE html>
<html lang="en">
<head>
<meta charset="utf-8">
<title>The Velvet Lantern Almanac Collection — Cover Spread</title>
<link rel="stylesheet" href="https://fonts.googleapis.com/css2?family=Manrope:wght@500;600;800&display=swap">
<style>
  :root {
    --paper: #ffffff;
    --cover-yellow: #fbec13;
    --ink: #222222;
    --grid-line: rgba(255, 255, 255, 0.45);
    --spine-text: #ffffff;
  }
  * { box-sizing: border-box; margin: 0; padding: 0; }
  html, body {
    width: 973px;
    height: 1200px;
    overflow: hidden;
    background: var(--paper);
  }
  .canvas {
    position: relative;
    width: 973px;
    height: 1200px;
    background: var(--paper);
  }
  .cover-spread {
    position: absolute;
    left: 105px;
    top: 25px;
    width: 763px;
    height: 555px;
    background: var(--cover-yellow);
    overflow: hidden;
  }
  .cover-grid {
    position: absolute;
    inset: 7px;
    background-image:
      repeating-linear-gradient(to right, var(--grid-line) 0 1px, transparent 1px 32px),
      repeating-linear-gradient(to bottom, var(--grid-line) 0 1px, transparent 1px 32px);
  }
  .back-cover-rule {
    position: absolute;
    left: 7px;
    top: 512px;
    width: 360px;
    height: 5px;
    background: var(--ink);
  }
  .barcode-area {
    position: absolute;
    left: 195px;
    top: 423px;
    width: 121px;
    height: 72px;
    background: #ffffff;
    border: 1px solid var(--ink);
    display: flex;
    align-items: center;
    justify-content: center;
    font-family: "Manrope", sans-serif;
    font-weight: 600;
    font-size: 14px;
    color: #000000;
  }
  .spine {
    position: absolute;
    left: 367px;
    top: 0;
    width: 28px;
    height: 555px;
    background: var(--ink);
  }
  .spine-bar {
    position: absolute;
    left: 12.5px;
    width: 3px;
    height: 62px;
    background: var(--spine-text);
  }
  .spine-bar--top { top: 67px; }
  .spine-bar--bottom { top: 426px; }
  .spine-title {
    position: absolute;
    left: 50%;
    top: 149px;
    transform: translateX(-50%);
    writing-mode: vertical-rl;
    font-family: "Manrope", sans-serif;
    font-weight: 500;
    font-size: 8.4px;
    letter-spacing: 1.55px;
    color: var(--spine-text);
    white-space: nowrap;
  }
  .front-title {
    position: absolute;
    left: 446px;
    top: 90px;
    font-family: "Manrope", sans-serif;
    font-weight: 800;
    font-size: 38px;
    line-height: 44px;
    letter-spacing: 1px;
    color: var(--ink);
    text-transform: uppercase;
  }
  .front-title__line { display: block; white-space: nowrap; }
  .front-cover-rule {
    position: absolute;
    left: 395px;
    top: 342px;
    width: 361px;
    height: 5px;
    background: var(--ink);
  }
  .front-subtitle {
    position: absolute;
    left: 448px;
    top: 397px;
    font-family: "Manrope", sans-serif;
    font-weight: 500;
    font-size: 16.5px;
    line-height: 23px;
    letter-spacing: 0.9px;
    color: var(--ink);
  }
</style>
</head>
<body>
  <main class="canvas">
    <section class="cover-spread" aria-label="Book cover spread: back cover, spine and front cover">
      <div class="cover-grid"></div>

      <div class="back-cover">
        <div class="barcode-area">for barcode</div>
        <div class="back-cover-rule"></div>
      </div>

      <div class="spine">
        <span class="spine-bar spine-bar--top"></span>
        <span class="spine-title">THE VELVET LANTERN ALMANAC COLLECTION</span>
        <span class="spine-bar spine-bar--bottom"></span>
      </div>

      <div class="front-cover">
        <h1 class="front-title">
          <span class="front-title__line">The</span>
          <span class="front-title__line">Velvet</span>
          <span class="front-title__line">Lantern</span>
          <span class="front-title__line">Almanac</span>
          <span class="front-title__line">Collection</span>
        </h1>
        <div class="front-cover-rule"></div>
        <p class="front-subtitle">Include Guerrilla Marketing.<br>Advertising, Branding and PR.</p>
      </div>
    </section>
  </main>
</body>
</html>
```